Lawn Company needs design work on a service call flyer!

We are a lawn care company that fertilizes and sprays lawns. This design is meant to be left behind at the customers house after a lawn application has been done too let them know what we have done.

The finished design will be printed on A6 paper (4.1 x 5.8 inches)

I have attached PDF files of the text that I want on the front of the document and the back of the document. I also included a sample design that I had been working on to give some idea what I would like. I don't want the same design, but you can use it as a building block for something new or come up with something entirely different.

FRONT: The front of the design is most important.

BACK: Other then the text the design should be minimal. If possible I would like an outline of the trees in my logo to be a backdrop. I have attached a PDF of the back of my business card as an example

The winning design will be a professional looking document that flows and reflects a lawn care business. Please contact me if you have any questions. I will only pick a design that is better then my current template.

Thank You

Target Market(s)

Lawn Care Customers

Industry/Entity Type

Lawn Care

Requirements
Must have
• 1. Our Logo
• 2. The attached text for the front & back of document
• 3. Our phone number (555-418-7390)
• 4. Our Email address (hollowfernturf@mailpost.example)
Nice to have
• A green theme with flowing graphics
Should not have
• any pictures of houses, people, or tools
• Don't copy the text or design from my design template. It is outdated, is it meant to be an example only

```html
<!DOCTYPE html>
<html lang="en">
<head>
<meta charset="utf-8">
<title>Hollowfern Turf Care – Service Call Notice</title>
<link rel="stylesheet" href="https://fonts.googleapis.com/css2?family=Roboto+Condensed:wght@400;700&family=Roboto:wght@700&display=swap">
<style>
  :root{
    --page-bg:#e8ebe7;
    --leaf:#5eb548;
    --leaf-deep:#1f5b3b;
    --mint:#e1efd5;
    --clay:#cd6a5f;
    --ink:#222;
    --paper:#fff;
  }
  *{box-sizing:border-box;margin:0;padding:0}
  html,body{width:1200px;height:1200px;overflow:hidden}
  body{background:var(--page-bg);font-family:"Roboto Condensed","Arial Narrow",sans-serif;color:var(--ink)}
  .flyer{position:absolute;left:197px;top:30px;width:806px;height:1140px;background:var(--paper);overflow:hidden;box-shadow:0 4px 18px rgba(0,0,0,.18)}
  .hero-photo{position:absolute;left:0;top:0;width:100%;height:350px;
    background:linear-gradient(180deg,#3f6e32 0%,#5d8f3c 35%,#7fbf45 70%,#5ea73a 100%)}
  .hero-rule{position:absolute;left:0;top:350px;width:100%;height:10px;background:var(--leaf)}
  .hero-rule-accent{position:absolute;left:0;top:364px;width:100%;height:3px;background:var(--clay)}
  .mint-panel{position:absolute;left:0;top:815px;width:100%;height:205px;background:var(--mint)}
  .footer-band{position:absolute;left:0;top:1020px;width:100%;height:120px;background:var(--leaf);border-top:4px solid var(--clay)}
  .brand{position:absolute;left:56px;top:395px;color:var(--leaf-deep);font-weight:700;font-size:34px;line-height:1.05;letter-spacing:.5px;text-transform:uppercase}
  .line{position:absolute;font-size:22px;white-space:nowrap;line-height:1}
  .blank{display:inline-block;border-bottom:1.5px solid var(--ink);height:18px;vertical-align:baseline}
  .app-date{left:330px;top:440px}
  .serviced{left:24px;top:497px}
  .section-title{position:absolute;left:24px;top:548px;font-family:Roboto,Arial,sans-serif;font-weight:700;font-size:23px;color:var(--leaf-deep)}
  .treatments{position:absolute;left:72px;top:610px;list-style:none;font-size:22px}
  .treatments li{position:relative;padding-left:18px;height:57px;white-space:nowrap}
  .treatments li::before{content:"";position:absolute;left:0;top:9px;width:8px;height:8px;border-radius:50%;background:var(--ink)}
  .watering{left:24px;top:781px}
  .promise{position:absolute;left:24px;top:838px;width:759px;font-size:19.5px;line-height:26px;text-align:justify}
  .contact{position:absolute;left:24px;top:1040px;color:#fff;font-size:32px;line-height:42px}
</style>
</head>
<body>
  <main class="flyer">
    <div class="hero-photo" role="img" aria-label="Photo of a manicured green lawn bordered by shrubs and trees"></div>
    <div class="hero-rule"></div>
    <div class="hero-rule-accent"></div>
    <div class="mint-panel"></div>
    <div class="footer-band"></div>

    <div class="brand">Hollowfern<br>Turf Care</div>

    <p class="line app-date">APPLICATION TIME / DATE:<span class="blank" style="width:208px"></span></p>
    <p class="line serviced">YOUR LAWN HAS BEEN PROFFESIONALLY SERVICED TODAY BY<span class="blank" style="width:198px"></span></p>

    <h2 class="section-title">Today's application consists of</h2>
    <ul class="treatments">
      <li>Seasonally Balanced Slow Release Fertilizer</li>
      <li>Broadleaf Weed Control (Please keep off the lawn until it is thoroughly dry)</li>
      <li>Other <span class="blank" style="width:490px"></span></li>
    </ul>

    <p class="line watering">Please begin watering the lawn <span class="blank" style="width:318px"></span> after application</p>

    <p class="promise">“We strive to complete work in a professional manner each and every visit. If you are not satisfied with the level of service you are receiving please contact us. We value your business and wish to maintain long-term relationships with our customers.”</p>

    <div class="contact">
      <p>Call us : 555-418-7390</p>
      <p>Email : hollowfernturf@mailpost.example</p>
    </div>
  </main>
</body>
</html>
```